Real Estate agent needs flyer/folder to contain bio and overview of services

I'm including files of the layout of the small folder. The folder is 6 1/2 across and 9 1/2 inches long. It will have a front & back cover and then writing on the 2 inside pages.

I am sending a few files to incorporate into the flyer, 1 new logo to use and 2 files which are coloring ideas.

Colors

Designer to choose colors to be used in the design.

```html
<!DOCTYPE html>
<html lang="en">
<head>
<meta charset="utf-8">
<title>Dana Marchetti – Realtor Folder</title>
<link href="https://fonts.googleapis.com/css2?family=Noto+Serif:wght@400;700&family=Source+Sans+3:ital,wght@0,400;0,600;1,400;1,600&display=swap" rel="stylesheet">
<style>
  :root{
    --stage:#e3e3e3;
    --cover:#ececec;
    --inner:#ffffff;
    --navy:#22358f;
    --ink:#1d1d1d;
    --brand-dot:#c8202f;
    --photo-green:#5f8a4a;
    --photo-sky:#3d6fb4;
    --photo-dusk:#283a6e;
    --photo-warm:#c9a060;
  }
  *{box-sizing:border-box;margin:0;padding:0}
  html,body{width:1200px;height:750px;overflow:hidden;background:var(--stage)}
  body{position:relative;font-family:"Source Sans 3",sans-serif;color:var(--ink)}
  .spread{position:absolute;top:163px;width:580px;height:424px;display:flex;box-shadow:0 10px 24px rgba(0,0,0,.12)}
  .spread--outer{left:12px}
  .spread--inner{left:608px}
  .page{position:relative;width:290px;height:424px}
  .spread--outer .page{background:var(--cover)}
  .spread--outer .page + .page{border-left:1px solid #dcdcdc}
  .spread--inner .page{background:var(--inner)}
  .spread--inner .page + .page{border-left:1px solid #ebebeb}
  h2{font-family:"Noto Serif",serif;color:var(--navy);font-weight:700;font-size:7.5px;line-height:1.3;margin-bottom:2px}
  p{font-size:5.2px;line-height:1.42;margin-bottom:4px}
  .sig{font-style:italic;font-weight:600}

  /* back cover */
  .back{padding:34px 18px 0 18px}
  .testimonials{display:flex;gap:10px}
  .testimonials .col:first-child{width:82px}
  .testimonials .col:last-child{width:88px;padding-top:6px}
  .back-note{position:absolute;left:18px;top:252px;width:130px;color:var(--navy);font-size:5.7px;line-height:1.4}
  .contact{position:absolute;left:18px;top:292px;color:var(--navy);font-size:6.6px;line-height:1.38}
  .brokerage{position:absolute;left:18px;top:345px;display:flex;align-items:center;gap:4px;color:var(--navy);font-size:6.5px;font-weight:600}
  .brokerage .dot{width:9px;height:9px;border-radius:50%;background:var(--brand-dot)}

  /* front cover */
  .front-name{position:absolute;left:0;right:0;top:165px;text-align:center;color:var(--navy);font-family:"Noto Serif",serif;font-weight:400}
  .front-name .name{font-size:16px;letter-spacing:1px;line-height:1.15}
  .front-name .role{font-size:4.5px;letter-spacing:.5px;margin-top:2px}
  .tagline{position:absolute;left:0;right:0;top:345px;text-align:center;font-family:"Noto Serif",serif;color:var(--navy);font-size:7.2px;line-height:1.3;letter-spacing:.2px}

  /* inner left */
  .intro{position:absolute;left:20px;top:18px;width:250px}
  .portrait{float:right;width:40px;height:46px;margin:0 0 4px 8px;background:linear-gradient(180deg,#f2efe9,#c9b69a 55%,#2a2a2a)}
  .intro h1{font-family:"Noto Serif",serif;color:var(--navy);font-weight:400;font-size:9.5px;margin-bottom:3px}
  .intro .clear{clear:both}
  .duo{position:absolute;left:20px;top:128px;width:250px;display:flex;gap:12px}
  .duo .col{width:119px}
  .sub{font-size:5.2px;font-weight:600;margin-bottom:4px}

  /* inner right */
  .services{position:absolute;left:18px;top:22px;width:256px;display:flex;gap:12px}
  .services .col{width:122px}

  /* photo band */
  .photos{position:absolute;left:0;top:237px;width:580px;height:187px;display:flex;gap:1px;background:#fff}
  .photo--entrance{width:355px;height:187px;background:linear-gradient(180deg,var(--photo-sky) 0%,var(--photo-green) 45%,#7a8c5a 70%,#6e9aa8 100%)}
  .photo-stack{display:flex;flex-direction:column;gap:1px;width:224px}
  .photo--villa{height:93px;background:linear-gradient(180deg,var(--photo-dusk),var(--photo-warm) 65%,#2e62a8)}
  .photo--lounge{height:93px;background:linear-gradient(135deg,#25366a,#7d87b0 55%,#d9c7a2)}
</style>
</head>
<body>

<section class="spread spread--outer" aria-label="Folder outer covers">
  <div class="page back">
    <h2>Testimonials:</h2>
    <div class="testimonials">
      <div class="col">
        <p>During the home buying process, Dana becomes your trusted advisor, mentor and friend. Her knowledge of the industry, community and market are best in class. A true professional! Dana aligned her goals with my own and understood the motivation behind my purchase. Dana is unequivocally the reason why I was able to purchase my home in Laguna Niguel and provide my family with a world-class community. Without her guidance and experience, I would still be in the market attempting to navigate the ever-changing work of real estate.</p>
        <p class="sig">Yasmin Calder</p>
      </div>
      <div class="col">
        <p>Dana is the kind of Real Estate professional everyone wants to represent them. She is knowledgeable, ethical, energetic, and follows up on every detail. Her honesty, integrity and expertise combined make her a very special and remarkable professional. We were lucky to find her!</p>
        <p class="sig">Howard &amp; Karen Miles</p>
        <p>Dana got us an amazing deal on our new home and sold our old home in a week. Dana is patient, hardworking, professional and most importantly HONEST. Dana is definitely one of the best in the business!</p>
        <p class="sig">Paige &amp; Aaron Lind</p>
      </div>
    </div>
    <p class="back-note">Along with being your Realtor, I’m a lifelong resource for all things home-related &amp; beyond… if you need a great referral for anything at all, call me! I can’t wait to work with you!</p>
    <div class="contact">
      Dana Marchetti<br>949 555 0148<br>hello@danamhomes.com<br>www.danamhomes.com
    </div>
    <div class="brokerage"><span class="dot"></span>Summit Realty</div>
  </div>

  <div class="page front">
    <div class="front-name">
      <div class="name">Dana Marchetti</div>
      <div class="role">REALTOR®</div>
    </div>
    <div class="tagline">HELPING PEOPLE SELL AND PURCHASE<br>HOMES IN SOUTHERN CALIFORNIA</div>
  </div>
</section>

<section class="spread spread--inner" aria-label="Folder inside pages">
  <div class="page">
    <div class="intro">
      <div class="portrait" role="img" aria-label="Portrait photo of the realtor"></div>
      <h1>Let me introduce myself</h1>
      <p>I’m originally from Chicago, but I’m a full-fledged California girl now. I’ve lived and worked in Orange County since 1996. I always say where we live is the next best thing to living on a tropical island. I’ve traveled to many and I’m always happy to come back to my Laguna Niguel home.</p>
      <p class="clear">My passion for this area is why I’m in Real Estate. I consider myself incredibly fortunate to sell homes and help people purchase homes in an area that I love with all my heart.</p>
      <p>This passion also carries over in representing my clients with the highest degree of professionalism, enthusiasm and care. My business is built on exceptional customer service and I’m grateful my clients are mostly repeat and referrals.</p>
    </div>
    <div class="duo">
      <div class="col">
        <h2>My Core Tenet</h2>
        <div class="sub">It’s All About YOU!</div>
        <p>My #1 priority is understanding YOUR needs and YOUR objectives. This understanding, along with working diligently on your behalf, means we accomplish your goal whether you’re purchasing your 1st home or selling a home you’ve loved so you can move on to the next chapter of your life.</p>
      </div>
      <div class="col">
        <h2>Real Estate Services<br>&amp; Beyond…</h2>
        <p>Simply put, I help people who are local, relocating and investing, sell and purchase homes in Southern California. For purchases outside of California, I can refer to a network of agents across the country.</p>
        <p>I also provide a team who is dedicated to providing outstanding customer service throughout the transaction. My team includes a network of lenders, title, and escrow officers, in house CPA, stagers, photographers, contractors and more.</p>
      </div>
    </div>
  </div>

  <div class="page">
    <div class="services">
      <div class="col">
        <h2>Selling your home</h2>
        <p>Selling your home is not like any other business transaction. It’s also personal. My priority as your Listing Agent is to guide you through what can be a complicated and sometimes emotional process.</p>
        <p>I place great emphasis on marketing your property with professional photographs, along with harnessing the power of the Internet and the virtual world to reach as many buyers as possible. Your property will be marketed to the public as well as to other agents, thus creating maximum exposure of your home.</p>
        <p>When we first meet to discuss selling your home, it’s essential for me to gain an understanding of your unique needs such as timelines, expectations and financial considerations, just to name a few. From there, I begin the process of listing and marketing your home. I lead you through negotiations and more paperwork than you ever care to do, guiding you to the successful closing of your home.</p>
      </div>
      <div class="col">
        <h2>Buying a home</h2>
        <p>If you’re thinking about buying a home, it’s imperative you have an accomplished, real estate professional by your side to walk you through what is likely the largest purchase of your life.</p>
        <p>To get started, I like to meet with you so we have an opportunity to get to know each other as purchasing a home is a uniquely, personal endeavor. At that time, we can discuss your goals and if it’s a good time for you to purchase a home.</p>
        <p>From there, the first step is to obtain a pre-approval from a lender. I’m able to recommend various lenders who can introduce and explain the various loan products available.</p>
        <p>After you’ve been pre-approved, that’s when the fun starts! I guide you through the home buying adventure every step of the way and look forward to handing you the keys to your new home.</p>
      </div>
    </div>
  </div>

  <div class="photos">
    <div class="photo photo--entrance" role="img" aria-label="Photo of a community entrance with palm trees, fountains and a bell tower"></div>
    <div class="photo-stack">
      <div class="photo photo--villa" role="img" aria-label="Photo of a luxury home at dusk with a lit pool"></div>
      <div class="photo photo--lounge" role="img" aria-label="Photo of a modern outdoor lounge beside a pool at twilight"></div>
    </div>
  </div>
</section>

</body>
</html>
```